Vossmer Collective - Business Card Design

several yrs ago
i have been one of the top 40 pellham photographers

when my fellow photo friends tried to join Pellham Visuals they were all rejected

Pellham Visuals told me if i formed some type of umbrella company of selected photographers they would offer me a contract as long as the portfolio images are stock worthy

so-i started the Vossmer Collective originally just for my friends and family and then grow the company to a few hundred photographers

after 4 yrs of working out all the bugs out
i will be offering other photographers to join the Vossmer Collective
------------

I now need a pro business card — retina website — an info pack about the Vossmer Collective

i bought the logo design from — https://www.markfoundry-example.com

i look at this logo as a group of independent silver balls with orange balls forming a larger group
- the Vossmer Collective
a group of independent members that will have their images sold thru Pellham Visuals - the worlds largest stack agency — under the Vossmer Collective name
--------

the look of the shadows and highlights in the logo

I want the fonts to have the similar look when it works

use the exact shade of orange and silver
I would like another to be the minor color ?

a contributor to Pellham Visuals - i want to really communicate this info
it makes my no name bus into something

please do not continue with this project

this project is on hold

in no order - information that should be part of the design - the most important part of the card - the bus name - VOSSMER COLLECTIVE - under Vossmer Collective you should have a creative tag line A contributor to Pellham Visuals - i like to see a 3d effect - refer to the website where i bought the logo - https://www.markfoundry-example.com - i included the Brink font that we used for the Vossmer Collective - incorporate this only if it helps the design - card stock - please include something other than wht - i have always liked a subtle translucent for background - only horizontal designs - one side of the card should have the logo and tag line together - use the symbols for phone mail etc.. - note the " i " in Vossmer Collective should be the same shade of orange - my card should have on this info - morris vossmer /founder / 717 555 0143 / website / email other card - tessa orbanek - her info is in the orig brief

Reason: this is my first time i have used a online site for design - only a few of the designs have the correct info none of the designs used the font that was included “brink” no one submitted a 3d feel to the designs - i need the card to have that Wow effect I just sent a more detailed brief to everyone thank you morris

Please - No more submissions

Target Market(s)

pro photographers and enthusiast

Industry/Entity Type

Business

Contact Information for Business Card

1. morris vossmer / founder -
2. tessa orbanek - 3. leon taverly
- i will add more names later

company - VOSSMER collective - tag line under logo? - in a script font - " a contributor to pellham visuals"

1. mv - no address for me

2. to - 418 E. 7th Street. Lower Marsden, NJ 08519. 609.555.0187. orbanek@inboxmail-example.com

I have several examples of what we started using their templates

Requirements
Must have
• the shadows and highlights in the logo

fonts to have the similar look when it works

Another color to be a minor color ?

i want this phrase to be included in the company name — "a contributor to Pellham Visuals"

it needs to be next to — floating around the logo — under the Vossmer Collective name anyway connecting it to the Vossmer Collective name
Nice to have
• i hope the folder names are somewhere attached to each file - if not - i will need review each file so you can understand what folder they belong to make sense of each file

i hope you get what i am trying to say
Should not have
• no address for morris vossmer

```html
<!DOCTYPE html>
<html lang="en">
<head>
<meta charset="utf-8">
<title>Vossmer Collective – Business Cards</title>
<link rel="stylesheet" href="https://fonts.googleapis.com/css2?family=Open+Sans:wght@400;600;700&family=Roboto+Condensed:wght@400;700&display=swap">
<style>
  :root {
    --backdrop: #ededed;
    --orange-deep: #b9450f;
    --orange-mid: #d35a13;
    --orange-light: #e26f1c;
    --slate: #56606b;
    --silver: #cfd3d8;
    --white: #ffffff;
    --cream: #f6dcc6;
  }
  * { box-sizing: border-box; margin: 0; padding: 0; }
  html, body {
    width: 1200px; height: 1001px; overflow: hidden;
    background: var(--backdrop);
  }
  .sheet {
    position: relative; width: 1200px; height: 1001px;
    display: flex; align-items: center; justify-content: center; gap: 40px;
  }
  .card {
    position: relative; width: 540px; height: 309px;
    background: radial-gradient(ellipse at 55% 40%, var(--orange-light) 0%, var(--orange-mid) 45%, var(--orange-deep) 100%);
    box-shadow: 0 6px 18px rgba(0,0,0,0.18);
    overflow: hidden;
  }
  .brand {
    position: absolute; display: flex; align-items: center; gap: 12px;
    font-family: "Open Sans", sans-serif; font-weight: 700;
    color: var(--slate); letter-spacing: 1px; white-space: nowrap;
  }
  .brand-dot {
    width: 30px; height: 30px; border-radius: 50%; background: var(--silver);
    flex: none;
  }
  .card-back .brand { left: 50%; top: 50%; transform: translate(-50%, -50%); font-size: 26px; }
  .card-front .brand { left: 34px; top: 46px; font-size: 21px; }
  .card-front .brand-dot { width: 24px; height: 24px; }
  .contact {
    position: absolute; left: 250px; top: 118px; color: var(--white);
  }
  .contact-name {
    font-family: "Open Sans", sans-serif; font-weight: 600; font-size: 21px;
  }
  .contact-role {
    font-family: "Roboto Condensed", sans-serif; font-weight: 700; font-size: 12px;
    color: var(--cream); margin-top: 2px;
  }
  .contact-company {
    font-family: "Open Sans", sans-serif; font-size: 15px; margin-top: 12px; letter-spacing: 0.5px;
  }
  .contact-tagline {
    font-family: "Open Sans", sans-serif; font-size: 10px; color: var(--cream); margin-top: 1px;
  }
  .contact-list { list-style: none; margin-top: 12px; }
  .contact-list li {
    display: flex; gap: 10px; align-items: flex-start;
    font-family: "Roboto Condensed", sans-serif; font-weight: 700; font-size: 13px; line-height: 17px;
    margin-bottom: 3px;
  }
  .contact-list svg { width: 14px; height: 14px; flex: none; margin-top: 1px; }
</style>
</head>
<body>
<main class="sheet">
  <section class="card card-front" aria-label="Business card front">
    <div class="brand"><span class="brand-dot"></span>VOSSMER COLLECTIVE</div>
    <div class="contact">
      <p class="contact-name">Tessa orbanek</p>
      <p class="contact-role">Partner</p>
      <p class="contact-company">VOSSMER collective</p>
      <p class="contact-tagline">a contributor to pellham visuals</p>
      <ul class="contact-list">
        <li>
          <svg viewBox="0 0 14 14" aria-hidden="true"><path d="M7 1a4 4 0 0 0-4 4c0 3 4 8 4 8s4-5 4-8a4 4 0 0 0-4-4zm0 5.5A1.5 1.5 0 1 1 7 3.5a1.5 1.5 0 0 1 0 3z" fill="#fff"/></svg>
          <span>418 E. 7th Street.<br>Lower Marsden, NJ 08519.</span>
        </li>
        <li>
          <svg viewBox="0 0 14 14" aria-hidden="true"><path d="M1 4c0-1 1-2 6-2s6 1 6 2v1.5h-3V4H4v1.5H1z M3 7h8l1 5H2z" fill="#fff"/></svg>
          <span>609.555.0187.</span>
        </li>
        <li>
          <svg viewBox="0 0 14 14" aria-hidden="true"><rect x="1" y="3" width="12" height="8" fill="#fff"/><path d="M1 3l6 5 6-5" fill="none" stroke="#d35a13" stroke-width="1.2"/></svg>
          <span>orbanek@inboxmail-example.com</span>
        </li>
      </ul>
    </div>
  </section>
  <section class="card card-back" aria-label="Business card back">
    <div class="brand"><span class="brand-dot"></span>VOSSMER COLLECTIVE</div>
  </section>
</main>
</body>
</html>
```